Business Card Design

Take existing logo/brand and develop business card for sales team.
We have two separate brands and require a business card for each.

1. VoxHarbor
2. MyNimbusLinko

Refer to our websites www.voxharbor.example.au and www.mynimbuslinko.example.au for designs currently implemented and in the marketplace.

Both cards are brands of our parent company Quorra Systems Pty Ltd - an Australian Telecommunications company in the medium business sector. We have only business customers, no retail/residential consumers.

Target Market(s)

Australian Business - small to medium enterprise

Industry/Entity Type

Business

Contact Information for Business Card

Lev Dorrit
Sales Director
Mobile: +61 400 555 187
Direct: +61 3 9555 0137
Email: lev@voxharbor.example.au
VoxHarbor (a brand of Quorra Systems Pty Ltd)

Lev Dorrit
Sales Director
Mobile: +61 400 555 187
Direct: +61 3 9555 0137
Email: lev@mynimbuslinko.example.au
MyNimbusLinko (a brand of Quorra Systems Pty Ltd)

Font styles to use
Sans Serif
Other font styles liked:
• Roboto Condensed, Open Sans

Requirements
Must have
• Clean lines, crisp fonts - suggest Roboto Condensed or similar.
• Must be easy to read and clear.
• Brand colour #0C8CCD
• Two colour maximum
Nice to have
• Modern, intellectual and unique design.
Should not have
• No die cuts
• No copies or rip-offs of other designs

```html
<!DOCTYPE html>
<html lang="en">
<head>
<meta charset="utf-8">
<title>MyNimbusLinko Business Card</title>
<link rel="stylesheet" href="https://fonts.googleapis.com/css2?family=Open+Sans:wght@400;600;700&display=swap">
<style>
  :root {
    --page-bg: #3a322e;
    --card-bg: #222325;
    --brand-blue: #0c8ccd;
    --text-white: #f2f2f2;
    --text-grey: #c9c9c9;
  }
  html, body {
    margin: 0;
    padding: 0;
    width: 1200px;
    height: 768px;
    overflow: hidden;
    background: var(--page-bg);
    font-family: "Open Sans", sans-serif;
  }
  .canvas {
    position: relative;
    width: 1200px;
    height: 768px;
  }
  .card {
    position: absolute;
    top: 226px;
    width: 520px;
    height: 316px;
    background: var(--card-bg);
    border-radius: 3px;
    box-shadow: 0 6px 18px rgba(0,0,0,0.35);
    overflow: hidden;
  }
  .card-front { left: 50px; }
  .card-back { left: 630px; }

  .front-brand {
    position: absolute;
    left: 0;
    right: 0;
    top: 128px;
    display: flex;
    align-items: center;
    justify-content: center;
    gap: 16px;
  }
  .brand-square {
    width: 40px;
    height: 40px;
    background: var(--brand-blue);
  }
  .front-brand .brand-name {
    font-size: 38px;
    font-weight: 400;
    color: var(--text-white);
    letter-spacing: 0.2px;
  }

  .back-mark {
    position: absolute;
    left: 36px;
    top: 88px;
    width: 140px;
    height: 140px;
    background: var(--brand-blue);
  }
  .back-details {
    position: absolute;
    left: 214px;
    top: 40px;
    right: 28px;
  }
  .back-brand .brand-name {
    display: block;
    font-size: 22px;
    font-weight: 400;
    color: var(--text-white);
    text-align: right;
  }
  .brand-tagline {
    display: block;
    font-size: 9px;
    color: var(--text-grey);
    text-align: right;
    margin-top: 1px;
  }
  .person-name {
    margin: 22px 0 0;
    font-size: 18px;
    font-weight: 700;
    color: var(--brand-blue);
  }
  .person-title {
    margin: 0;
    font-size: 12px;
    color: var(--text-grey);
  }
  .contact-list {
    list-style: none;
    margin: 22px 0 0;
    padding: 0;
  }
  .contact-list li {
    display: flex;
    align-items: center;
    gap: 10px;
    font-size: 13px;
    line-height: 22px;
    color: var(--text-white);
  }
  .contact-icon {
    width: 12px;
    height: 12px;
    flex: none;
    fill: var(--brand-blue);
  }
</style>
</head>
<body>
<div class="canvas">

  <section class="card card-front" aria-label="Card front">
    <div class="front-brand">
      <span class="brand-square"></span>
      <span class="brand-name">MyNimbusLinko</span>
    </div>
  </section>

  <section class="card card-back" aria-label="Card back">
    <div class="back-mark"></div>
    <div class="back-details">
      <div class="back-brand">
        <span class="brand-name">MyNimbusLinko</span>
        <span class="brand-tagline">a brand of Quorra Systems Pty Ltd</span>
      </div>
      <p class="person-name">Lev Dorrit</p>
      <p class="person-title">Sales Director</p>
      <ul class="contact-list">
        <li>
          <svg class="contact-icon" viewBox="0 0 12 12"><rect x="3" y="0" width="6" height="12" rx="1"/><rect x="4" y="1.5" width="4" height="7" fill="#222325"/></svg>
          +61 400 555 187
        </li>
        <li>
          <svg class="contact-icon" viewBox="0 0 12 12"><path d="M1 4 Q6 0 11 4 L9.5 5.5 L8 4.5 L4 4.5 L2.5 5.5 Z"/><rect x="2" y="6" width="8" height="5" rx="1"/></svg>
          +61 3 9555 0137
        </li>
        <li>
          <svg class="contact-icon" viewBox="0 0 12 12"><rect x="0" y="2" width="12" height="8"/><path d="M0 2 L6 7 L12 2" fill="none" stroke="#222325" stroke-width="1"/></svg>
          lev@mynimbuslinko.example.au
        </li>
        <li>
          <svg class="contact-icon" viewBox="0 0 12 12"><circle cx="6" cy="6" r="6"/><path d="M0 6 H12 M6 0 V12" stroke="#222325" stroke-width="0.8"/></svg>
          www.mynimbuslinko.example.au
        </li>
      </ul>
    </div>
  </section>

</div>
</body>
</html>
```